Medical equipment business looking for professional, unique business card

We need a business card design for a durable medical equipment company. We are small but would like our cards to express that we are much bigger. We focus on braces (back, knee, wrist, etc) but also do crutches, rollators, wheelchairs- basically medical equipment that gets you going and back in Action. Our colors are blue and green and our logo has an arrow and use of a "spine". We'd like to express professionalism while being unique.

Industry/Entity Type

Medical Equipment

Contact Information for Business Card

Professional feel but unique. Memorable.

Font styles to use
Serif
Sans Serif
Other font styles liked:
• verdana

Requirements
Must have
• card holders cell#, business phone#, fax#, email, website address, business address, logo
Nice to have
• use of medical/healthcare related descriptive words, items, look
Should not have
• the wrong colors or cartoon characters.

```html
<!DOCTYPE html>
<html lang="en">
<head>
<meta charset="utf-8">
<title>Kinetra DME — Business Card</title>
<link href="https://fonts.googleapis.com/css2?family=Open+Sans:wght@400;600&display=swap" rel="stylesheet">
<style>
  :root {
    --bg: #1e1f21;
    --paper: #ffffff;
    --brand-blue: #2f6d8f;
    --deep-blue: #1d4f73;
    --brand-green: #8cc63f;
    --ink: #555a5e;
    --rule: #8b8f93;
  }
  * { box-sizing: border-box; margin: 0; padding: 0; }
  html, body { width: 1200px; height: 950px; overflow: hidden; }
  body {
    background: var(--bg);
    font-family: "Open Sans", Verdana, sans-serif;
    position: relative;
  }
  .card {
    position: absolute;
    left: 250px;
    width: 700px;
    height: 400px;
    border-radius: 4px;
    overflow: hidden;
  }
  .card--front { top: 55px; background: var(--paper); }
  .card--back { top: 495px; background: var(--brand-green); }

  .edge-stripe {
    position: absolute; left: 0; right: 0; bottom: 0; height: 10px;
    background: linear-gradient(to bottom, var(--brand-green) 0 40%, var(--deep-blue) 40% 100%);
  }

  .brand {
    position: absolute;
    display: flex; flex-direction: column; align-items: flex-start;
  }
  .brand__row { display: flex; align-items: center; gap: 12px; }
  .brand__dot { width: 18px; height: 18px; border-radius: 50%; background: var(--brand-green); }
  .brand__name { font-weight: 600; font-size: 40px; color: var(--brand-blue); letter-spacing: 0.5px; }
  .brand__tag { font-weight: 600; font-size: 14px; color: var(--brand-blue); margin-left: 30px; margin-top: 2px; }

  .card--front .brand { left: 230px; top: 70px; }

  .divider {
    position: absolute; left: 60px; right: 60px; top: 190px;
    height: 1px; background: var(--rule);
  }

  .person { position: absolute; left: 60px; top: 215px; }
  .person__name { font-size: 22px; color: var(--brand-blue); }
  .person__role { font-size: 16px; color: var(--brand-green); margin-top: 2px; }

  .contacts { position: absolute; left: 60px; top: 285px; list-style: none; }
  .contacts li {
    display: flex; align-items: center; gap: 12px;
    font-size: 15px; color: var(--ink); line-height: 23px;
  }
  .contacts svg { width: 15px; height: 15px; fill: var(--brand-blue); flex: none; }

  .address {
    position: absolute; right: 60px; top: 215px; text-align: right;
    font-size: 15px; color: var(--ink); line-height: 24px; font-style: normal;
  }

  .card--back .brand { left: 210px; top: 150px; }
  .card--back .brand__name,
  .card--back .brand__tag { color: var(--paper); }
  .card--back .brand__dot { background: var(--paper); }
  .back-web {
    position: absolute; left: 26px; top: 50%;
    transform: translateY(-50%);
    writing-mode: vertical-rl;
    font-size: 13px; letter-spacing: 5px; color: var(--paper);
    white-space: nowrap;
  }
</style>
</head>
<body>
  <section class="card card--front" aria-label="Business card front">
    <div class="brand">
      <div class="brand__row"><span class="brand__dot"></span><span class="brand__name">Kinetra DME</span></div>
      <span class="brand__tag">Durable Medical Equipment</span>
    </div>
    <div class="divider"></div>
    <div class="person">
      <p class="person__name">Daniel Ward</p>
      <p class="person__role">President</p>
    </div>
    <ul class="contacts">
      <li><svg viewBox="0 0 16 16"><path d="M2 5c0-2 2-3 6-3s6 1 6 3v1h-3V5H5v1H2zM3 7h10l1 7H2z"/></svg>555 201 4417</li>
      <li><svg viewBox="0 0 16 16"><path d="M4 1h8v14H4zM5.5 2.5v9h5v-9z"/></svg>555 308 6290</li>
      <li><svg viewBox="0 0 16 16"><path d="M4 1h8v4H4zM1 6h14v8H1zM4 10h8v3H4z"/></svg>555 412 7735</li>
      <li><svg viewBox="0 0 16 16"><path d="M1 3h14v10H1zM2 4l6 5 6-5v-.5H2z" fill-rule="evenodd"/></svg>daniel@kinetradme.com</li>
    </ul>
    <address class="address">
      4120 Harbor Lane<br>
      Glen Ridge, NY 10550<br>
      www.kinetradme.com
    </address>
    <div class="edge-stripe"></div>
  </section>

  <section class="card card--back" aria-label="Business card back">
    <div class="brand">
      <div class="brand__row"><span class="brand__dot"></span><span class="brand__name">Kinetra DME</span></div>
      <span class="brand__tag">Durable Medical Equipment</span>
    </div>
    <p class="back-web">www.kinetradme.com</p>
  </section>
</body>
</html>
```